Heal the world with your creativity.

We're looking for advertising materials (social media, email, etc) for a new mental health platform called PIM (www.seepim.example). PIM’s mission is to empower our members to heal and thrive by making expert advice and real-life experiences accessible to all.

Note

Facebook Cover Images: 820 x 312 pixels
LinkedIn Cover Images: 1128 x 191 pixels
3 x Social Media Post Image Templates: 1080 x 1080 pixles
3 x Enewsletter Header Image Templates: 1080 x 360 pixels
Sales One sheet: US Letter (8.5 x 11 inches)
Overview Powerpoint template: 13.33 x 7.5 inches

Fonts to Use:
Galanogrotesque
Montserrat regular

Target Market(s)

18 - 35 year olds

Industry/Entity Type

Mental Health

Requirements
Must have
• Facebook Cover Images: 820 x 312 pixels
3 x Enewsletter Header Images: 1080 x 360 pixels

Fonts to Use:
Galanogrotesque
Montserrat regular
Nice to have
• Creative copywriting for social media posts

```html
<!DOCTYPE html>
<html lang="en">
<head>
<meta charset="utf-8">
<title>PIM — Community of Support</title>
<link rel="stylesheet" href="https://fonts.googleapis.com/css2?family=Montserrat:wght@400&family=Poppins:wght@600;800&display=swap">
<style>
  :root {
    --orange: #f07f35;
    --navy: #0d4166;
    --sky: #5d9fd0;
    --mist: #c9ccd0;
    --white: #ffffff;
    --photo-warm: #d9b08c;
    --photo-deep: #6e5845;
  }
  html, body {
    margin: 0;
    padding: 0;
    width: 1200px;
    height: 527px;
    overflow: hidden;
    background: var(--orange);
  }
  .banner {
    position: relative;
    width: 1200px;
    height: 527px;
    overflow: hidden;
    background: var(--orange);
  }
  .banner__shapes {
    position: absolute;
    inset: 0;
    width: 1200px;
    height: 527px;
  }
  .banner__wordmark {
    position: absolute;
    left: -14px;
    bottom: -62px;
    margin: 0;
    font-family: "Poppins", sans-serif;
    font-weight: 600;
    font-size: 330px;
    line-height: 1;
    letter-spacing: -12px;
    color: var(--orange);
  }
  .banner__headline {
    position: absolute;
    left: 150px;
    top: 34px;
    margin: 0;
    font-family: "Poppins", sans-serif;
    font-weight: 800;
    font-size: 60px;
    line-height: 62px;
    letter-spacing: 1px;
    text-transform: uppercase;
    color: var(--white);
  }
  .banner__subline {
    position: absolute;
    left: 152px;
    top: 266px;
    margin: 0;
    font-family: "Montserrat", sans-serif;
    font-weight: 400;
    font-size: 27px;
    line-height: 32px;
    color: var(--white);
  }
</style>
</head>
<body>
  <main class="banner">
    <svg class="banner__shapes" viewBox="0 0 1100 483" preserveAspectRatio="none" aria-hidden="false">
      <defs>
        <linearGradient id="photo-tone" x1="0" y1="0" x2="1" y2="1">
          <stop offset="0" stop-color="var(--photo-deep)"/>
          <stop offset="0.5" stop-color="var(--photo-warm)"/>
          <stop offset="1" stop-color="#b98a66"/>
        </linearGradient>
      </defs>
      <circle class="shape-navy-disc" cx="190" cy="405" r="215" fill="var(--navy)"/>
      <circle class="photo-circle" cx="880" cy="170" r="242" fill="url(#photo-tone)" role="img" aria-label="Photo of two young friends sharing a warm, smiling hug"/>
      <circle class="shape-mist-disc" cx="680" cy="10" r="112" fill="var(--mist)" opacity="0.7"/>
      <circle class="shape-sky-disc" cx="1080" cy="420" r="155" fill="var(--sky)" opacity="0.85"/>
    </svg>

    <p class="banner__wordmark" aria-label="PIM">pim</p>

    <h1 class="banner__headline">Is a full<br>community<br>of support:</h1>

    <p class="banner__subline">Affordable, always accessible,<br>and with you in the moment<br>when you need it most</p>
  </main>
</body>
</html>
```